Title Company
Stationary for Title Company
Project: Title Company
Title Company  - Real Estate
Creative Brief
Professional
Tobias Renwald
27308 SW 62nd Ave Suite 118 Cedar Hollow, Fl. 33987
tobiasrenwald@quillmarsh.com
www.harrowfieldrealestategroup.com

```html
<!DOCTYPE html>
<html lang="en">
<head>
<meta charset="utf-8">
<title>Brambleoak Deeds – Business Card</title>
<link href="https://fonts.googleapis.com/css2?family=Cinzel:wght@400;600&display=swap" rel="stylesheet">
<style>
  :root {
    --page-bg: #e9ebee;
    --card-white: #ffffff;
    --brand-blue: #1f5c93;
    --brand-blue-deep: #174a7a;
    --band-dark: #3d4147;
    --band-grey: #8c9299;
    --ink-white: #ffffff;
    --card-shadow: rgba(20, 30, 45, 0.18);
  }
  * { box-sizing: border-box; margin: 0; padding: 0; }
  html, body { width: 1200px; height: 874px; overflow: hidden; }
  body {
    background: var(--page-bg);
    font-family: "Cinzel", "Times New Roman", serif;
    position: relative;
  }
  .card {
    position: absolute;
    width: 560px;
    height: 320px;
    background: var(--card-white);
    border-radius: 26px;
    overflow: hidden;
    box-shadow: 0 10px 28px var(--card-shadow);
  }
  .card--back { left: 580px; top: 100px; }
  .card--front { left: 70px; top: 450px; }

  .wordmark {
    position: absolute;
    display: flex;
    align-items: center;
    gap: 10px;
    color: var(--brand-blue);
    font-weight: 600;
    letter-spacing: 0.06em;
    white-space: nowrap;
  }
  .wordmark__square {
    width: 22px;
    height: 22px;
    background: var(--brand-blue);
  }
  .card--back .wordmark { left: 50%; top: 96px; transform: translateX(-50%); font-size: 26px; }
  .card--back .website {
    position: absolute;
    left: 0; right: 0; top: 196px;
    text-align: center;
    font-size: 10px;
    letter-spacing: 0.14em;
    color: var(--brand-blue);
  }

  .card--front .wordmark { left: 118px; top: 62px; font-size: 23px; }
  .wave { position: absolute; inset: 0; }
  .holder-name {
    position: absolute;
    right: 48px;
    top: 112px;
    font-size: 15px;
    letter-spacing: 0.06em;
    color: var(--brand-blue);
    white-space: nowrap;
  }
  .contact-list {
    position: absolute;
    left: 22px;
    top: 196px;
    list-style: none;
    color: var(--ink-white);
    font-size: 9.5px;
    letter-spacing: 0.05em;
    line-height: 17px;
    white-space: nowrap;
  }
  .contact-list li { display: flex; align-items: center; gap: 6px; }
  .contact-list li.is-continued { padding-left: 16px; }
  .contact-icon {
    width: 10px; height: 10px;
    border-radius: 50%;
    background: var(--ink-white);
    flex: none;
    display: flex; align-items: center; justify-content: center;
  }
  .contact-icon svg { width: 7px; height: 7px; }
</style>
</head>
<body>

  <section class="card card--back" aria-label="Card back">
    <div class="wordmark"><span class="wordmark__square"></span><span>Brambleoak Deeds</span></div>
    <p class="website">www.harrowfieldrealestategroup.com</p>
  </section>

  <section class="card card--front" aria-label="Card front">
    <svg class="wave" viewBox="0 0 560 320" preserveAspectRatio="none" aria-hidden="true">
      <path d="M0,150 C130,118 220,232 350,212 C450,196 500,150 560,132 L560,152 C500,170 450,214 350,228 C220,246 130,136 0,166 Z" fill="var(--band-grey)"/>
      <path d="M0,166 C130,136 220,246 350,228 C450,214 500,170 560,152 L560,170 C500,188 450,232 350,244 C220,262 130,154 0,182 Z" fill="var(--band-dark)"/>
      <path d="M0,182 C130,154 220,262 350,244 C450,232 500,188 560,170 L560,320 L0,320 Z" fill="var(--brand-blue)"/>
      <path d="M0,260 C150,240 320,300 560,250 L560,320 L0,320 Z" fill="var(--brand-blue-deep)" opacity="0.45"/>
    </svg>

    <div class="wordmark"><span class="wordmark__square"></span><span>Brambleoak Deeds</span></div>
    <p class="holder-name">Tobias Renwald</p>

    <ul class="contact-list">
      <li><span class="contact-icon"><svg viewBox="0 0 10 10"><path d="M5 1a3 3 0 0 0-3 3c0 2.2 3 5 3 5s3-2.8 3-5a3 3 0 0 0-3-3z" fill="var(--brand-blue)"/></svg></span>27308 SW 62nd Ave Suite 118</li>
      <li class="is-continued">Cedar Hollow, Fl. 33987</li>
      <li><span class="contact-icon"><svg viewBox="0 0 10 10"><path d="M2 1h2l1 2.5-1.2.8a5 5 0 0 0 2 2l.8-1.2L9 6v2a1 1 0 0 1-1 1A7 7 0 0 1 1 2a1 1 0 0 1 1-1z" fill="var(--brand-blue)"/></svg></span>305 555 0142</li>
      <li><span class="contact-icon"><svg viewBox="0 0 10 10"><path d="M2 1h2l1 2.5-1.2.8a5 5 0 0 0 2 2l.8-1.2L9 6v2a1 1 0 0 1-1 1A7 7 0 0 1 1 2a1 1 0 0 1 1-1z" fill="var(--brand-blue)"/></svg></span>305 555 0187</li>
      <li><span class="contact-icon"><svg viewBox="0 0 10 10"><rect x="1" y="2.5" width="8" height="5" fill="var(--brand-blue)"/></svg></span>tobiasrenwald@quillmarsh.com</li>
      <li><span class="contact-icon"><svg viewBox="0 0 10 10"><circle cx="5" cy="5" r="3.5" fill="none" stroke="var(--brand-blue)" stroke-width="1.2"/></svg></span>www.harrowfieldrealestategroup.com</li>
    </ul>
  </section>

</body>
</html>
```